Product Packaging Redesign

We have an existing package layout that needs to be redesigned to include our product name, Brisk Woofer, our UPC and more appealing/professional designs.

Changes will include artwork, images, SKU, product details and description etc.

Product campaign can be viewed here http://briskwoofer.example

You can get details, images etc from there.

Looking for retail friendly design, appealing to buyers.
Updates

Industry/Entity Type

Retail

Colors

Designer to choose colors to be used in the design.

Requirements
Must have
• Package renamed to Brisk Woofer
UPC changed to ours (see attached file)
Clean, appealing retail design
Nice to have
• Logo for Brisk Woofer created/added to package

```html
<!DOCTYPE html>
<html lang="en">
<head>
<meta charset="utf-8">
<title>Brisk Woofer – Box Dieline</title>
<link href="https://fonts.googleapis.com/css2?family=Arimo:wght@400;700&display=swap" rel="stylesheet">
<style>
  :root {
    --paper: #ffffff;
    --cut-line: #9a9a9a;
    --water-deep: #1567c0;
    --water-mid: #2f93dc;
    --water-light: #6cc2f0;
    --deck: #eceeee;
    --brand-blue: #1a6fd0;
    --brand-orange: #f39a1e;
    --banner: #ffffff;
    --photo-dark: #1c2126;
    --photo-mid: #3b444c;
    --mark-grey: #5a5a5a;
  }
  html, body {
    margin: 0;
    padding: 0;
    width: 1200px;
    height: 563px;
    overflow: hidden;
    background: var(--paper);
  }
  .dieline {
    display: block;
    width: 1200px;
    height: 563px;
    font-family: "Arimo", Arial, sans-serif;
  }
  .cut { fill: var(--paper); stroke: var(--cut-line); stroke-width: 0.8; }
  .fold { stroke: var(--cut-line); stroke-width: 0.6; fill: none; }
  .spec-heading { fill: #fff; font-size: 11px; font-weight: 700; }
  .spec-item { fill: #fff; font-size: 9.4px; }
  .brand-name { fill: var(--brand-orange); font-weight: 700; }
  .side-title { font-size: 16px; font-weight: 700; }
  .side-title--light { fill: #fff; }
  .side-title--blue { fill: var(--brand-blue); }
  .badge-text { fill: var(--brand-blue); font-size: 8.5px; font-weight: 700; }
  .lid-badge-text { fill: #fff; font-size: 7px; font-weight: 700; }
  .mark { fill: var(--mark-grey); }
</style>
</head>
<body>
<svg class="dieline" viewBox="0 0 1200 563" xmlns="http://www.w3.org/2000/svg">
  <defs>
    <linearGradient id="water" x1="0" y1="0" x2="0.3" y2="1">
      <stop offset="0" stop-color="var(--water-deep)"/>
      <stop offset="0.5" stop-color="var(--water-mid)"/>
      <stop offset="1" stop-color="var(--water-light)"/>
    </linearGradient>
    <linearGradient id="photo" x1="0" y1="0" x2="0" y2="1">
      <stop offset="0" stop-color="var(--photo-mid)"/>
      <stop offset="1" stop-color="var(--photo-dark)"/>
    </linearGradient>
  </defs>

  <g class="box-net">
    <!-- glue flap -->
    <path class="cut" d="M500 130 L458 138 L458 402 L500 410 Z"/>

    <!-- back panel -->
    <g class="back-panel">
      <rect x="500" y="130" width="278" height="280" fill="url(#water)" role="img" aria-label="Pool water surface photograph"/>
      <rect x="500" y="350" width="278" height="60" fill="var(--deck)" opacity="0.85"/>
      <text class="spec-heading" x="522" y="149">Specification</text>
      <text class="spec-item" x="514" y="164">• IP67 dustproof &amp; waterproof wireless speaker</text>
      <text class="spec-item" x="514" y="174">• Built in rechargeable battery</text>
      <text class="spec-item" x="514" y="184">• Portable delicate design</text>
      <text class="spec-item" x="514" y="194">• Wireless audio transmission</text>
      <text class="spec-item" x="514" y="204">• Built in Microphone</text>
      <text class="spec-item" x="514" y="214">• With phone hands free calling</text>
      <text class="spec-item" x="514" y="224">• With suction cup</text>
      <text class="spec-item" x="514" y="234">• Charging by USB through computer</text>
      <text class="spec-heading" x="522" y="251">Accessory</text>
      <text class="spec-item" x="514" y="265">• Waterproof wireless speaker</text>
      <text class="spec-item" x="514" y="275">• USB charger cable</text>
      <text class="spec-item" x="514" y="285">• User manual</text>
      <rect x="508" y="300" width="116" height="108" rx="40" fill="url(#photo)" role="img" aria-label="Product photograph of the waterproof speaker"/>
      <text class="brand-name" x="630" y="320" font-size="22">BRISK</text>
      <text class="brand-name" x="630" y="345" font-size="22">WOOFER</text>
      <rect x="695" y="358" width="42" height="22" fill="#fff"/>
      <rect class="mark" x="690" y="384" width="11" height="9"/>
      <rect class="mark" x="708" y="384" width="11" height="9"/>
      <circle class="mark" cx="737" cy="388.5" r="5"/>
      <circle class="mark" cx="756" cy="388.5" r="5"/>
    </g>
    <!-- back bottom flaps -->
    <path class="cut" d="M500 410 L778 410 L778 493 Q778 500 771 500 L507 500 Q500 500 500 493 Z"/>
    <line class="fold" x1="500" y1="460" x2="778" y2="460"/>

    <!-- spine -->
    <rect x="778" y="130" width="48" height="280" fill="url(#water)" role="img" aria-label="Pool water surface photograph"/>
    <text class="side-title side-title--light" transform="translate(795 142) rotate(90)">Waterproof Wireless Speakers</text>
    <path class="cut" d="M778 130 L778 88 L786 88 L826 110 L826 130 Z"/>
    <path class="cut" d="M778 410 L826 410 L826 446 L786 452 L778 452 Z"/>

    <!-- top tuck flap and lid -->
    <path class="cut" d="M826 80 L826 46 Q826 38 834 38 L1092 38 Q1100 38 1100 46 L1100 80 Z"/>
    <rect x="826" y="80" width="274" height="50" fill="url(#water)" role="img" aria-label="Pool water surface photograph"/>
    <text class="brand-name" x="848" y="102" font-size="18">BRISK</text>
    <text class="brand-name" x="848" y="122" font-size="18">WOOFER</text>
    <circle cx="1053" cy="103" r="7" fill="#fff"/>
    <text class="lid-badge-text" transform="translate(1065 84) rotate(90)">Waterproof</text>
    <text class="lid-badge-text" transform="translate(1074 84) rotate(90)">Wireless</text>
    <text class="lid-badge-text" transform="translate(1083 84) rotate(90)">Speakers</text>

    <!-- front panel -->
    <g class="front-panel">
      <rect x="826" y="130" width="274" height="280" fill="url(#water)" role="img" aria-label="Pool water surface photograph"/>
      <rect x="826" y="335" width="274" height="75" fill="var(--deck)"/>
      <path d="M836 152 L1090 140 L1085 246 L842 251 Z" fill="var(--banner)"/>
      <text class="brand-name" x="864" y="192" font-size="38">BRISK</text>
      <text class="brand-name" x="864" y="232" font-size="38">WOOFER</text>
      <rect x="884" y="260" width="128" height="140" rx="46" fill="url(#photo)" role="img" aria-label="Product photograph of the waterproof speaker"/>
      <circle cx="1068" cy="358" r="8" fill="var(--brand-blue)"/>
      <text class="badge-text" x="1068" y="382" text-anchor="middle">Waterproof</text>
      <text class="badge-text" x="1068" y="391" text-anchor="middle">Wireless</text>
      <text class="badge-text" x="1068" y="400" text-anchor="middle">Speakers</text>
    </g>

    <!-- right side panel -->
    <rect class="cut" x="1100" y="130" width="55" height="280"/>
    <text class="side-title side-title--blue" transform="translate(1122 142) rotate(90)">Waterproof Wireless Speakers</text>
    <path class="cut" d="M1100 130 L1100 86 L1150 86 L1155 96 L1155 130 Z"/>
    <path class="cut" d="M1100 410 L1155 410 L1155 446 L1110 452 L1100 452 Z"/>
  </g>
</svg>
</body>
</html>
```